Full book cover design for FEEDBACK book

The book title is: Feedback
Subtitle: Seek it, give it, connect with it.
Authors: Carl Brenner & Marian Quist
We are looking for a complete book cover design using a combination of my brand colours and that of my co-author (Carl). The colours we use include:

Marian: Blue #1E84AB & Carl: Blue #01275B and white.

An idea on the wording for the back cover is here (open to tweak/shorten it if better that way):

The most dynamic leaders today are focused on increasing effectiveness and improving team cohesion. This book demonstrates how creating a culture of feedback enables both of these things.

Feedback allows for the strengthening of communication and allows individuals to continually learn and grow, with the support of their colleagues.

Marian and Carl have created a unique approach to change the often-negative perception associated with feedback. They created it for you…to unlock the opportunity, freedom and success you can achieve when feedback is implemented and used regularly.

If you are a leader looking for ways to build skills in your people, contribute to their growth and development, and maintain a strong, supportive culture, all while delivering business outcomes, then this is the book for you.

“If you are keen to transform feedback from average to awesome and from being a chore to an art, this book is a must read.”
Victor Lunsky, Bravelane Axton

“In today’s hybrid work environment, greater transparency and empowerment, through developing a feedback culture, is essential.”
Odette Varley, Pelvro

We will also need to allow space for a barcode and the publishers logo (just above it) on the back bottom right hand side.

Target Market(s)

Business leaders

Industry/Entity Type

Business

Font styles to use
Serif
Other font styles liked:
• Open to any other fonts that will suit the design

Colors
0054AA
0677BA
7BADD7
CADEEF
E8F1F8

Requirements
Must have
• Colours: Blue #1E84AB & Blue #01275B and white.
Nice to have
• Something creative and smart but not too busy.

```html
<!DOCTYPE html>
<html lang="en">
<head>
<meta charset="utf-8">
<title>Feedback — Book Cover</title>
<link rel="stylesheet" href="https://fonts.googleapis.com/css2?family=Gelasio:wght@400;500&display=swap">
<style>
  :root {
    --navy: #01275b;
    --navy-soft: #1a3f73;
    --brand-blue: #1e84ab;
    --paper: #ffffff;
    --shadow: #e9e9e9;
    --curl-dark: #d6d6d6;
  }
  * { margin: 0; padding: 0; box-sizing: border-box; }
  html, body { width: 840px; height: 1200px; overflow: hidden; background: var(--paper); }
  .cover {
    position: relative;
    width: 840px;
    height: 1200px;
    background: var(--paper);
    font-family: "Gelasio", Georgia, serif;
    color: var(--navy);
  }
  .speech-cluster {
    position: absolute;
    left: 226px;
    top: 142px;
    width: 410px;
    height: 352px;
  }
  .title {
    position: absolute;
    left: 0;
    width: 840px;
    top: 478px;
    text-align: center;
    font-size: 121px;
    font-weight: 400;
    letter-spacing: 1px;
    line-height: 1;
    padding-left: 6px;
  }
  .paper-shade {
    position: absolute;
    left: 0;
    top: 700px;
    width: 840px;
    height: 270px;
    background: radial-gradient(ellipse 60% 45% at 50% 50%, var(--shadow) 0%, rgba(240,240,240,0.5) 55%, rgba(255,255,255,0) 100%);
  }
  .tear-strip {
    position: absolute;
    left: 196px;
    top: 770px;
    width: 446px;
    height: 110px;
    background: var(--paper);
    box-shadow: inset 0 4px 6px rgba(0,0,0,0.06), inset 0 -4px 6px rgba(0,0,0,0.05);
  }
  .curl {
    position: absolute;
    top: 778px;
    width: 24px;
    height: 102px;
    border-radius: 12px;
    box-shadow: 0 8px 10px rgba(0,0,0,0.12);
  }
  .curl--left {
    left: 172px;
    background: linear-gradient(90deg, #f4f4f4 0%, #ffffff 40%, var(--curl-dark) 100%);
  }
  .curl--right {
    left: 642px;
    background: linear-gradient(90deg, var(--curl-dark) 0%, #ffffff 60%, #f2f2f2 100%);
  }
  .subtitle {
    position: absolute;
    left: 194px;
    width: 450px;
    top: 815px;
    text-align: center;
    font-size: 22px;
    font-weight: 500;
    letter-spacing: 0.1px;
    white-space: nowrap;
  }
  .author-band {
    position: absolute;
    left: 0;
    top: 1088px;
    width: 840px;
    height: 62px;
    background: var(--navy);
    display: flex;
    align-items: center;
    justify-content: center;
  }
  .authors {
    color: var(--paper);
    font-size: 29px;
    font-weight: 400;
  }
</style>
</head>
<body>
<main class="cover">
  <svg class="speech-cluster" viewBox="0 0 410 352" role="img" aria-label="Speech bubble composed of many small chat and profile icons">
    <defs>
      <linearGradient id="clusterTone" x1="0" y1="0" x2="1" y2="1">
        <stop offset="0" stop-color="#01275b"/>
        <stop offset="1" stop-color="#1a3f73"/>
      </linearGradient>
    </defs>
    <path d="M30 22 Q36 2 70 4 L330 2 Q364 4 366 34 L368 250 Q366 280 336 282 L340 282 L406 350 L330 290 L40 292 Q6 290 4 260 L2 60 Q4 30 30 22 Z" fill="url(#clusterTone)" opacity="0.9"/>
  </svg>

  <h1 class="title">Feedback</h1>

  <div class="paper-shade"></div>
  <div class="tear-strip"></div>
  <div class="curl curl--left"></div>
  <div class="curl curl--right"></div>
  <p class="subtitle">SEEK IT, GIVE IT, CONNECT WITH IT</p>

  <footer class="author-band">
    <p class="authors">Carl Brenner &amp; Marian Quist</p>
  </footer>
</main>
</body>
</html>
```